High End Art Gallery Business Card

We're looking for a business card design that is elegant and artful. Foil embossing, blind embossed pattern, or some kind of "extra" element to make it stand out. Standard American size. The back should remain blank or nearly blank so that notes can be written on the back.
Please check our website at elsintandor.com to see information about our gallery and the type of artwork that we sell.
Included with the files is a brand identity guideline. In addition to the colors listed, we like to incorporate an indigo blue. The business card design in the guideline seems too simplistic. I have included some photos of other business card designs that have caught my eye.
thank you!

Contact Information for Business Card

Mirela Tandor
Gallery Owner
remaining details are in the attached docs

Requirements
Nice to have
• some kind of natural/organic element to reflect the hand-made nature of all of the original artwork.

```html
<!DOCTYPE html>
<html lang="en">
<head>
<meta charset="utf-8">
<title>Elsin Tandor Gallery – Business Card</title>
<link href="https://fonts.googleapis.com/css2?family=Montserrat:wght@600&family=Work+Sans:wght@400&display=swap" rel="stylesheet">
<style>
  :root {
    --backdrop: #262626;
    --gold: #b38845;
    --paper: #ffffff;
    --ink: #3a3a3a;
  }
  html, body {
    margin: 0;
    width: 1200px;
    height: 900px;
    overflow: hidden;
    background: var(--backdrop);
  }
  .stage {
    position: relative;
    width: 1200px;
    height: 900px;
  }
  .card {
    position: absolute;
    left: 290px;
    width: 620px;
    height: 354px;
    box-shadow: 0 10px 30px rgba(0,0,0,.45);
    box-sizing: border-box;
  }
  .card--front {
    top: 52px;
    background: var(--gold);
    display: flex;
    flex-direction: column;
    align-items: center;
    justify-content: center;
    gap: 22px;
  }
  .card--back {
    top: 450px;
    background: var(--paper);
    display: flex;
    align-items: center;
  }
  .brand-name {
    font-family: "Work Sans", sans-serif;
    font-weight: 400;
    letter-spacing: .16em;
    text-transform: uppercase;
    margin: 0;
  }
  .card--front .brand-name {
    color: var(--paper);
    font-size: 21px;
  }
  .brand-disc {
    display: block;
  }
  .back-brand {
    display: flex;
    align-items: center;
    gap: 18px;
    width: 300px;
    padding-left: 34px;
    box-sizing: border-box;
  }
  .card--back .brand-name {
    color: var(--ink);
    font-size: 16px;
    line-height: 1.4;
  }
  .divider {
    width: 2px;
    height: 186px;
    background: var(--gold);
    margin-right: 26px;
  }
  .contact {
    font-family: "Work Sans", sans-serif;
    color: var(--ink);
  }
  .contact__name {
    font-family: "Montserrat", sans-serif;
    font-weight: 600;
    color: var(--gold);
    font-size: 30px;
    letter-spacing: .04em;
    text-transform: uppercase;
    margin: 0;
    line-height: 1.1;
  }
  .contact__role {
    font-size: 17px;
    letter-spacing: .04em;
    margin: 2px 0 14px;
  }
  .contact__address {
    font-style: normal;
    font-size: 17px;
    line-height: 1.4;
    letter-spacing: .04em;
    margin-bottom: 10px;
  }
  .contact__line {
    display: flex;
    align-items: center;
    gap: 10px;
    font-size: 18px;
    letter-spacing: .04em;
    line-height: 1.45;
  }
  .contact__line svg { flex: none; }
  .accent { color: var(--gold); }
</style>
</head>
<body>
<div class="stage">

  <section class="card card--front">
    <svg class="brand-disc" width="140" height="140" viewBox="0 0 140 140" aria-hidden="true">
      <circle cx="70" cy="70" r="68" fill="var(--paper)"/>
    </svg>
    <p class="brand-name">Elsin Tandor Gallery</p>
  </section>

  <section class="card card--back">
    <div class="back-brand">
      <svg class="brand-disc" width="80" height="80" viewBox="0 0 80 80" aria-hidden="true">
        <circle cx="40" cy="40" r="39" fill="var(--gold)"/>
      </svg>
      <p class="brand-name">Elsin Tandor<br>Gallery</p>
    </div>

    <div class="divider"></div>

    <div class="contact">
      <h1 class="contact__name">Mirela Tandor</h1>
      <p class="contact__role">Gallery Owner</p>
      <address class="contact__address">412 Kalena Street<br>Hilo, HI 96720 USA</address>
      <div class="contact__line">
        <svg width="13" height="13" viewBox="0 0 24 24" aria-hidden="true"><path d="M6.6 10.8a15 15 0 0 0 6.6 6.6l2.2-2.2a1 1 0 0 1 1-.25 11.4 11.4 0 0 0 3.6.57 1 1 0 0 1 1 1V20a1 1 0 0 1-1 1A17 17 0 0 1 3 4a1 1 0 0 1 1-1h3.5a1 1 0 0 1 1 1c0 1.25.2 2.45.57 3.57a1 1 0 0 1-.25 1z" fill="var(--gold)"/></svg>
        <span>(808) 555-0142</span>
      </div>
      <div class="contact__line">
        <svg width="13" height="13" viewBox="0 0 24 24" aria-hidden="true"><rect x="2" y="5" width="20" height="14" rx="1" fill="none" stroke="var(--gold)" stroke-width="2"/><path d="M2 6l10 7 10-7" fill="none" stroke="var(--gold)" stroke-width="2"/></svg>
        <span>info@elsintandor.com</span>
      </div>
      <div class="contact__line">
        <svg width="13" height="13" viewBox="0 0 24 24" aria-hidden="true"><circle cx="12" cy="12" r="10" fill="none" stroke="var(--gold)" stroke-width="2"/><path d="M2 12h20M12 2c3 3 3 17 0 20M12 2c-3 3-3 17 0 20" fill="none" stroke="var(--gold)" stroke-width="1.6"/></svg>
        <span>www.<span class="accent">elsintandor</span>.com</span>
      </div>
    </div>
  </section>

</div>
</body>
</html>
```